An eCommerce Business Needs a Wordpress Web Design and Development

We need a website design and development for a new eCommerce business based in New York called "Velvet Orra". We sell items that are based on satisfying multi-sensory pathways of the person, as we believe that all is interconnected forming the Universal Language. All our products are made of raw natural elements from earth or the cosmos. The final design should communicate visual-perceptive pathways that produce harmonious effects and creativity.
Updates

Dear Designers, Please accept my sincere apology for my delayed response. I am currently in the midst of extensive business travelling while at the same time gathering feedback from online polling with friends as the website potential end-users. I shall get back to you by May 12 or sooner. Thank you for your understanding.

Target Market(s)

Art, fossils, minerals and numismatic collectors.

Industry/Entity Type

Online Shopping

Coding

Coded - Design and coding required

Number of Pages Required

5+ page

Font styles to use
Sans Serif
Script

Colors

Designer to choose colors to be used in the design.

Requirements
Must have
• - Simple and clean design.
• - Desktop and mobile device friendly.
• - Photos and images of string musical instruments, crystals, numismatics and cultural artefacts.
• - A blog page.
• - A check-out cart for online shopping and payment. Example: https://store.plumwick.com
• - Standard links to social media.

```html
<!DOCTYPE html>
<html lang="en">
<head>
<meta charset="utf-8">
<title>Velvet Orra — Home</title>
<link href="https://fonts.googleapis.com/css2?family=Raleway:wght@400;500;600;700;800&family=Open+Sans:ital,wght@0,400;0,600;0,700;1,400&display=swap" rel="stylesheet">
<style>
:root{
  --ink:#1b1b1b;
  --olive:#8b7b22;
  --navy:#24406e;
  --logo:#6c86a8;
  --hero-bg:#e9e9e9;
  --line:#e3e3e3;
  --tab-off:#cfcfcf;
  --news-bg:#f3f3f3;
  --foot-bg:#262626;
  --foot-text:#b9b9b9;
  --white:#ffffff;
}
*{box-sizing:border-box;margin:0;padding:0}
html,body{width:1200px;height:2727px;overflow:hidden;background:var(--white)}
body{position:relative;font-family:"Open Sans",Arial,sans-serif;color:var(--ink)}
.abs{position:absolute}

/* Header */
.site-header{position:absolute;left:0;top:0;width:1200px;height:136px}
.brand{left:160px;top:34px;width:140px;font-family:"Raleway",sans-serif;font-weight:600;font-size:30px;line-height:36px;letter-spacing:3px;color:var(--logo);text-transform:uppercase}
.search{left:633px;top:31px;width:280px;height:33px;border:1px solid #dadada;background:#f4f4f4;display:flex;align-items:center;justify-content:space-between;padding:0 10px;font-style:italic;font-size:11px;color:#777}
.cart{left:945px;top:31px;display:flex;align-items:center;gap:8px}
.cart-icon{width:28px;height:28px;border-radius:50%;background:var(--navy);display:flex;align-items:center;justify-content:center}
.cart-label{font-size:10px;font-weight:700;line-height:13px;text-transform:uppercase}
.cart-label span{color:var(--navy)}
.main-nav{left:365px;top:95px;width:671px;display:flex;justify-content:space-between;font-size:12px;font-weight:600;text-transform:uppercase;white-space:nowrap}
.header-rule{left:0;top:131px;width:1200px;height:5px;border-top:2px solid #3b3b3b;border-bottom:1px solid #3b3b3b}

/* Hero */
.hero{left:0;top:136px;width:1200px;height:528px;background:var(--hero-bg)}
.hero-visual{left:218px;top:109px;width:346px;height:310px;border-radius:40% 55% 45% 50%;background:radial-gradient(ellipse at 55% 60%,#b8541c 0%,#8e3a12 45%,rgba(233,233,233,0) 72%)}
.hero-copy{left:600px;top:176px;width:393px;text-align:right;font-family:"Raleway",sans-serif}
.hero-kicker{font-size:46px;font-weight:600;color:#3d3d3d;letter-spacing:1px;line-height:56px}
.hero-offer{display:flex;justify-content:flex-end;align-items:center;gap:10px;margin-top:2px}
.hero-pct{font-size:100px;font-weight:800;color:var(--olive);line-height:100px}
.hero-sale{text-align:left;color:#2e2e2e}
.hero-sale b{display:block;font-size:58px;font-weight:600;line-height:58px}
.hero-sale small{display:block;font-size:16px;font-weight:700;letter-spacing:2px}
.hero-dots{left:578px;top:463px;display:flex;gap:4px}
.hero-dots i{width:13px;height:13px;border-radius:50%;background:#9a9a9a}
.hero-dots i:last-child{background:#555}
.hero-rule{left:0;top:664px;width:1200px;height:5px;border-top:2px solid var(--navy);border-bottom:2px solid var(--olive)}

/* Tabs & products */
.tabs{left:0;top:718px;width:1200px;display:flex;justify-content:center;gap:44px;font-family:"Raleway",sans-serif;font-size:24px;font-weight:600;text-transform:uppercase}
.tabs span{color:var(--tab-off)}
.tabs span.active{color:var(--ink)}
.product{width:204px;height:348px;border:1px solid var(--line);text-align:center;background:var(--white)}
.product-media{height:238px;border-bottom:1px solid var(--line)}
.product-price{margin-top:18px;font-size:12.5px;font-weight:700;color:var(--olive)}
.product-name{margin-top:6px;font-size:11px;font-weight:600;text-transform:uppercase}
.product-actions{margin-top:12px;display:flex;justify-content:center;gap:8px}
.product-actions i{width:28px;height:28px;border:1px solid #9a9a9a;border-radius:50%;display:flex;align-items:center;justify-content:center}

/* About */
.about{left:160px;top:1574px;width:876px;height:377px;border:1px solid #dcdcdc;background:linear-gradient(90deg,#f7f7f8,#eef0f4)}
.about-media{left:30px;top:40px;width:420px;height:300px;background:radial-gradient(ellipse at 45% 50%,#8a4a26 0%,#6b3419 35%,rgba(240,241,244,0) 70%)}
.about-copy{left:485px;top:70px;width:362px}
.about-copy h2{font-family:"Raleway",sans-serif;font-size:25px;font-weight:600;text-transform:uppercase;margin-bottom:16px}
.about-copy p{font-size:10.5px;line-height:23px;color:#2a2a2a}
.btn-outline{display:inline-block;margin-top:22px;width:97px;height:32px;border:2px solid var(--navy);color:var(--navy);font-size:10.5px;font-weight:700;text-transform:uppercase;text-align:center;line-height:28px}

/* Help band */
.help{left:0;top:2022px;width:1200px;height:183px;background:var(--olive);color:var(--white)}
.help h2{position:absolute;top:34px;width:1200px;text-align:center;font-family:"Raleway",sans-serif;font-size:23px;font-weight:700;text-transform:uppercase;letter-spacing:.5px}
.help-items{left:160px;top:94px;width:880px;display:flex;justify-content:space-between}
.help-item{display:flex;align-items:center;gap:12px}
.help-item b{display:block;font-family:"Raleway",sans-serif;font-size:17px;font-weight:700}
.help-item small{font-size:11.5px}
.help-arrow{top:98px}

/* Newsletter */
.newsletter{left:0;top:2205px;width:1200px;height:191px;background:var(--news-bg);text-align:center}
.newsletter h2{margin-top:32px;font-family:"Raleway",sans-serif;font-size:27px;font-weight:500}
.newsletter p{margin-top:8px;font-size:12.5px;color:#333}
.signup{position:absolute;left:344px;top:109px;display:flex}
.signup-field{width:434px;height:42px;border:1px solid #dedede;background:var(--white);text-align:left;padding-left:12px;font-style:italic;font-size:10.5px;line-height:40px;color:#666}
.signup-btn{width:78px;height:42px;background:var(--olive);color:var(--white);font-size:12px;font-weight:700;line-height:42px;text-transform:uppercase}

/* Footer */
.site-footer{left:0;top:2396px;width:1200px;height:331px;background:var(--foot-bg);color:var(--foot-text)}
.foot-col{top:36px}
.foot-col h3{font-family:"Raleway",sans-serif;font-size:15.5px;font-weight:600;color:var(--white)}
.foot-col h3::after{content:"";display:block;width:20px;height:2px;background:var(--olive);margin-top:14px}
.foot-col ul{list-style:none;margin-top:20px;font-size:11px;line-height:20px}
.contact-row{display:flex;gap:14px;align-items:flex-start;font-size:11px;line-height:18px;margin-bottom:12px}
.contact-row i{flex:none;width:22px;height:22px;border:1px solid #777;border-radius:50%;display:flex;align-items:center;justify-content:center}
.contact-row .mail{color:var(--olive)}
.foot-rule{left:162px;top:262px;width:876px;height:1px;background:#3d3d3d}
.socials{left:150px;top:278px;display:flex;gap:8px}
.socials i{width:25px;height:25px;border-radius:50%}
.copyright{right:160px;top:286px;font-size:10.5px;color:#8a8a8a;display:flex;gap:14px;white-space:nowrap}
</style>
</head>
<body>

<header class="site-header">
  <div class="abs brand">Velvet Orra</div>
  <div class="abs search">Enter Keyword...
    <svg width="13" height="13" viewBox="0 0 13 13"><circle cx="5.5" cy="5.5" r="4" fill="none" stroke="#222" stroke-width="1.8"/><line x1="8.5" y1="8.5" x2="12" y2="12" stroke="#222" stroke-width="2"/></svg>
  </div>
  <div class="abs cart">
    <span class="cart-icon"><svg width="14" height="13" viewBox="0 0 14 13"><path d="M1 1h2l2 7h6l2-5H4" fill="none" stroke="#fff" stroke-width="1.5"/><circle cx="6" cy="11" r="1.2" fill="#fff"/><circle cx="10" cy="11" r="1.2" fill="#fff"/></svg></span>
    <span class="cart-label">Shopping<br>Cart <span>$0.00</span></span>
  </div>
  <nav class="abs main-nav">
    <span>Musical Instruments</span><span>Crystals</span><span>Numismatic Collectibles</span><span>Cultural Artifacts</span><span>About Us</span>
  </nav>
  <div class="abs header-rule"></div>
</header>

<section class="abs hero">
  <div class="abs hero-visual" role="img" aria-label="Photo of a violin with bow"></div>
  <div class="abs hero-copy">
    <div class="hero-kicker">NEW ARRIVALS</div>
    <div class="hero-offer">
      <span class="hero-pct">70%</span>
      <span class="hero-sale"><b>SALE</b><small>OFFER TODAY</small></span>
    </div>
  </div>
  <div class="abs hero-dots"><i></i><i></i><i></i></div>
</section>
<div class="abs hero-rule"></div>

<div class="abs tabs"><span class="active">Popular Products</span><span>Best Sellers</span><span>Specials</span></div>

<svg width="0" height="0" style="position:absolute">
  <defs>
    <symbol id="ico-cart" viewBox="0 0 14 13"><path d="M1 1h2l2 7h6l2-5H4" fill="none" stroke="#555" stroke-width="1.2"/><circle cx="6" cy="11" r="1" fill="#555"/><circle cx="10" cy="11" r="1" fill="#555"/></symbol>
    <symbol id="ico-heart" viewBox="0 0 14 13"><path d="M7 12L1.8 6.6A3 3 0 017 2.6a3 3 0 015.2 4z" fill="none" stroke="#555" stroke-width="1.2"/></symbol>
    <symbol id="ico-compare" viewBox="0 0 14 13"><path d="M2 4h10M2 9h10M9 1.5l3 2.5-3 2.5M5 6.5L2 9l3 2.5" fill="none" stroke="#555" stroke-width="1.2"/></symbol>
  </defs>
</svg>

<article class="abs product" style="left:160px;top:789px"><div class="product-media" role="img" aria-label="Photo of an acoustic guitar" style="background:radial-gradient(ellipse at 50% 55%,#d8a76a 0%,#f1f1f1 45%)"></div><div class="product-price">$ 50.00</div><div class="product-name">Musical Instruments</div><div class="product-actions"><i><svg width="13" height="12"><use href="#ico-cart"/></svg></i><i><svg width="13" height="12"><use href="#ico-heart"/></svg></i><i><svg width="13" height="12"><use href="#ico-compare"/></svg></i></div></article>
<article class="abs product" style="left:386px;top:789px"><div class="product-media" role="img" aria-label="Photo of a quartz crystal cluster" style="background:radial-gradient(ellipse at 50% 50%,#cfc9c4 0%,#f1f1f1 45%)"></div><div class="product-price">$ 50.00</div><div class="product-name">Crystals</div><div class="product-actions"><i><svg width="13" height="12"><use href="#ico-cart"/></svg></i><i><svg width="13" height="12"><use href="#ico-heart"/></svg></i><i><svg width="13" height="12"><use href="#ico-compare"/></svg></i></div></article>
<article class="abs product" style="left:610px;top:789px"><div class="product-media" role="img" aria-label="Photo of two silver coins" style="background:radial-gradient(ellipse at 50% 50%,#b8b8b8 0%,#f1f1f1 48%)"></div><div class="product-price">$ 25.00</div><div class="product-name">Numismatic Collectibles</div><div class="product-actions"><i><svg width="13" height="12"><use href="#ico-cart"/></svg></i><i><svg width="13" height="12"><use href="#ico-heart"/></svg></i><i><svg width="13" height="12"><use href="#ico-compare"/></svg></i></div></article>
<article class="abs product" style="left:834px;top:789px"><div class="product-media" role="img" aria-label="Photo of an ancient terracotta warrior figure" style="background:radial-gradient(ellipse at 50% 50%,#7c7268 0%,#f1f1f1 40%)"></div><div class="product-price">$ 50.00</div><div class="product-name">Cultural Artifacts</div><div class="product-actions"><i><svg width="13" height="12"><use href="#ico-cart"/></svg></i><i><svg width="13" height="12"><use href="#ico-heart"/></svg></i><i><svg width="13" height="12"><use href="#ico-compare"/></svg></i></div></article>

<article class="abs product" style="left:160px;top:1156px"><div class="product-media" role="img" aria-label="Photo of a black acoustic guitar" style="background:radial-gradient(ellipse at 50% 55%,#1f1f1f 0%,#f1f1f1 42%)"></div><div class="product-price">$ 50.00</div><div class="product-name">Musical Instruments</div><div class="product-actions"><i><svg width="13" height="12"><use href="#ico-cart"/></svg></i><i><svg width="13" height="12"><use href="#ico-heart"/></svg></i><i><svg width="13" height="12"><use href="#ico-compare"/></svg></i></div></article>
<article class="abs product" style="left:386px;top:1156px"><div class="product-media" role="img" aria-label="Photo of a clear and amethyst crystal" style="background:radial-gradient(ellipse at 45% 55%,#8a6aa0 0%,#cfd3da 25%,#f1f1f1 48%)"></div><div class="product-price">$ 50.00</div><div class="product-name">Crystals</div><div class="product-actions"><i><svg width="13" height="12"><use href="#ico-cart"/></svg></i><i><svg width="13" height="12"><use href="#ico-heart"/></svg></i><i><svg width="13" height="12"><use href="#ico-compare"/></svg></i></div></article>
<article class="abs product" style="left:610px;top:1156px"><div class="product-media" role="img" aria-label="Photo of a vintage nickel coin" style="background:radial-gradient(circle at 50% 50%,#8f8f8f 0%,#a8a8a8 30%,#f1f1f1 46%)"></div><div class="product-price">$ 25.00</div><div class="product-name">Numismatic Collectibles</div><div class="product-actions"><i><svg width="13" height="12"><use href="#ico-cart"/></svg></i><i><svg width="13" height="12"><use href="#ico-heart"/></svg></i><i><svg width="13" height="12"><use href="#ico-compare"/></svg></i></div></article>
<article class="abs product" style="left:834px;top:1156px"><div class="product-media" role="img" aria-label="Photo of a dark bronze statue" style="background:radial-gradient(ellipse at 50% 50%,#2f3338 0%,#f1f1f1 45%)"></div><div class="product-price">$ 50.00</div><div class="product-name">Cultural Artifacts</div><div class="product-actions"><i><svg width="13" height="12"><use href="#ico-cart"/></svg></i><i><svg width="13" height="12"><use href="#ico-heart"/></svg></i><i><svg width="13" height="12"><use href="#ico-compare"/></svg></i></div></article>

<section class="abs about">
  <div class="abs about-media" role="img" aria-label="Photo of violins, violas and bows arranged together"></div>
  <div class="abs about-copy">
    <h2>About Us</h2>
    <p>Velvet Orra is a dedicated company, which foundation is based on an integrative view of the Universe. We seek items from all over the world, carefully selected to meet high standards of our merchandise. We sell items that are based on satisfying multi-sensory pathways of the person, as we believe that all is interconnected forming the Universal Language. All our products are made of raw natural elements</p>
    <span class="btn-outline">Read More</span>
  </div>
</section>

<section class="abs help">
  <h2>How Can We Help You?</h2>
  <svg class="abs help-arrow" style="left:118px" width="14" height="24" viewBox="0 0 14 24"><path d="M12 2L2 12l10 10" fill="none" stroke="#d8cf9c" stroke-width="2"/></svg>
  <svg class="abs help-arrow" style="left:1070px" width="14" height="24" viewBox="0 0 14 24"><path d="M2 2l10 10L2 22" fill="none" stroke="#d8cf9c" stroke-width="2"/></svg>
  <div class="abs help-items">
    <div class="help-item">
      <svg width="46" height="54" viewBox="0 0 46 54"><rect x="3" y="2" width="40" height="42" rx="7" fill="#fff"/><rect x="8" y="10" width="30" height="15" fill="#8b7b22"/><circle cx="12" cy="35" r="3" fill="#8b7b22"/><circle cx="34" cy="35" r="3" fill="#8b7b22"/><rect x="6" y="44" width="8" height="8" fill="#fff"/><rect x="32" y="44" width="8" height="8" fill="#fff"/></svg>
      <div><b>Free Shipping</b><small>Ducimus qui blanditiis</small></div>
    </div>
    <div class="help-item">
      <svg width="38" height="46" viewBox="0 0 38 46"><path d="M9 20v-7a10 10 0 0120 0v7" fill="none" stroke="#fff" stroke-width="5"/><rect x="2" y="20" width="34" height="25" rx="2" fill="#fff"/></svg>
      <div><b>100% Secure</b><small>Ducimus qui blanditiis</small></div>
    </div>
    <div class="help-item">
      <svg width="56" height="40" viewBox="0 0 56 40"><rect x="7" y="2" width="42" height="28" rx="2" fill="none" stroke="#fff" stroke-width="3"/><path d="M1 33h54l-4 5H5z" fill="#fff"/></svg>
      <div><b>Best Online</b><small>Ducimus qui blanditiis</small></div>
    </div>
    <div class="help-item">
      <svg width="58" height="46" viewBox="0 0 58 46"><circle cx="29" cy="12" r="9" fill="#fff"/><circle cx="11" cy="17" r="6" fill="#fff"/><circle cx="47" cy="17" r="6" fill="#fff"/><path d="M14 46c0-14 6-22 15-22s15 8 15 22z" fill="#fff"/><path d="M1 42c0-10 4-16 10-16 3 0 5 1 6 3-2 4-3 8-3 13z" fill="#fff"/><path d="M57 42c0-10-4-16-10-16-3 0-5 1-6 3 2 4 3 8 3 13z" fill="#fff"/></svg>
      <div><b>Customer Support</b><small>Ducimus qui blanditiis</small></div>
    </div>
  </div>
</section>

<section class="abs newsletter">
  <h2>Newsletter</h2>
  <p>Sign up for our mailing list to get latest updates and offers</p>
  <div class="signup"><div class="signup-field">Email Address:</div><div class="signup-btn">Signup</div></div>
</section>

<footer class="abs site-footer">
  <div class="abs foot-col" style="left:162px;width:230px">
    <h3>Store Information</h3>
    <div style="margin-top:22px">
      <div class="contact-row"><i><svg width="10" height="12" viewBox="0 0 10 12"><path d="M5 11S1 6.5 1 4.5a4 4 0 018 0C9 6.5 5 11 5 11z" fill="none" stroke="#aaa"/><circle cx="5" cy="4.5" r="1.3" fill="#aaa"/></svg></i><span>Orra Studio, 18 Heron Lane<br>54321 Heronvale France</span></div>
      <div class="contact-row"><i><svg width="11" height="11" viewBox="0 0 11 11"><path d="M2 1l2 2-1 1.5a6 6 0 003.5 3.5L8 7l2 2-1.5 1.5C5 10 1 6 .5 2.5z" fill="#aaa"/></svg></i><span>Call us now: 0987-654-312</span></div>
      <div class="contact-row"><i><svg width="11" height="9" viewBox="0 0 11 9"><rect x=".5" y=".5" width="10" height="8" fill="none" stroke="#aaa"/><path d="M.5 .5l5 4 5-4" fill="none" stroke="#aaa"/></svg></i><span class="mail">Email: hello@velvetorra.shop</span></div>
    </div>
  </div>
  <div class="abs foot-col" style="left:416px">
    <h3>Categories</h3>
    <ul><li>Musical Instruments</li><li>Crystals</li><li>Numismatic Collectibles</li><li>Cultural Artifacts</li></ul>
  </div>
  <div class="abs foot-col" style="left:602px">
    <h3>Information</h3>
    <ul><li>Specials</li><li>New products</li><li>Best sellers</li><li>Our stores</li><li>Contact us</li><li>About us</li></ul>
  </div>
  <div class="abs foot-col" style="left:764px">
    <h3>My Account</h3>
    <ul><li>My orders</li><li>My credit slips</li><li>My addresses</li><li>My personal info</li></ul>
  </div>
  <div class="abs foot-col" style="left:922px">
    <h3>Customer Care</h3>
    <ul><li>Order Info</li><li>Shipping / Tracking Info</li><li>Returns Info</li><li>Request Exchange</li><li>Guarantee</li></ul>
  </div>
  <div class="abs foot-rule"></div>
  <div class="abs socials" aria-label="Social media links">
    <i style="background:#3b5a9a"></i><i style="background:#1da1f2"></i><i style="background:#3f729b"></i><i style="background:#dd4b39"></i><i style="background:#cb2027"></i><i style="background:#c4302b"></i>
  </div>
  <div class="abs copyright"><span>Copyright © 2018 Velvet Orra. All Rights reserved</span><span>Privacy Policy</span><span>Terms &amp; Conditions</span></div>
</footer>

</body>
</html>
```